Velo Dash Compact Speed Karts

We are looking for a full web site for our race car category that allows us to edit and update some of the content. We would like the site to feel modern and attractive with the following features: 1. Event calender (with the ability for us to update) 2. Social media/ vid hub links 3. photo gallery (with the ability for us to update) 4. Member area with log in access (controlled access) - this area to include access to category regulations for up to 5 types of cars separately 5. Championship ladder for up to 5 different groups 6. sponsor page and sponsors scrolling across bottom of all pages. Please find attached our logo to be used and for reference on color/ style 7. page to show merchandise but no need for a store.

Industry/Entity Type

Motor racing category

Coding

Coded - Design and coding required

Number of Pages Required

5+ page

Colors
0054AA
0677BA
7BADD7
CADEEF
E8F1F8
FFF300
FFF600
FEFA6F
FFFEC7
FFFEE8
EB3D1F
EC4F4E
F09395
F8D3D4
FCEDEE

Requirements
Must have
• Ability to update calender/photo gallery/championship ladder including points/ notice board - Members section

```html
<!DOCTYPE html>
<html lang="en">
<head>
<meta charset="utf-8">
<title>Velo Dash Compact Speed Karts</title>
<link rel="stylesheet" href="https://fonts.googleapis.com/css2?family=Poppins:wght@400;500;600&family=Russo+One&family=Teko:wght@500;600&display=swap">
<style>
:root{
  --blue:#2140ad;
  --blue-deep:#12288a;
  --blue-bright:#2556d8;
  --red:#e8261c;
  --yellow:#f9d62e;
  --ink:#151515;
  --text:#222;
  --muted:#444;
  --grey-bg:#f3f3f3;
  --footer:#1b1b1b;
  --white:#fff;
}
*{margin:0;padding:0;box-sizing:border-box}
html,body{width:1200px;height:4181px;overflow:hidden}
body{font-family:"Poppins",sans-serif;color:var(--text);background:var(--white)}
section,header,footer{position:relative;width:1200px}
.abs{position:absolute}
.photo{display:block}
.btn{display:flex;align-items:center;justify-content:center;font-family:"Russo One",sans-serif;font-size:13px;letter-spacing:.3px;text-transform:uppercase}
.btn-yellow{background:var(--yellow);color:var(--ink)}
.section-title{font-family:"Russo One",sans-serif;font-variant:small-caps;font-size:40px;color:var(--ink);text-align:center;letter-spacing:1px}
.rule{height:4px;width:82px;background:var(--blue)}
.arrow{width:26px;height:44px}

/* header */
.site-header{height:122px;background:var(--white)}
.brand{left:75px;top:28px;width:200px;height:70px;display:flex;align-items:center;gap:10px;border:3px solid var(--ink);border-radius:8px;padding:0 10px}
.brand-mark{width:18px;height:18px;background:var(--red);flex:none}
.brand-name{font-family:"Poppins",sans-serif;font-weight:600;font-size:14px;line-height:1.15;color:var(--blue)}
.util-nav{top:30px;left:752px;display:flex;gap:26px;font-size:11.5px;font-weight:500;color:#333}
.login{left:990px;top:20px;width:137px;height:36px;background:var(--blue);color:var(--white);font-size:11.5px;font-weight:500;display:flex;align-items:center;justify-content:center}
.main-nav{top:80px;left:447px;display:flex;gap:35px;font-size:13px;font-weight:500;color:#222}
.main-nav .current{color:var(--red)}

/* hero */
.hero{height:616px;overflow:hidden}
.hero-photo{position:absolute;inset:0;background:linear-gradient(180deg,#b9c6c4 0%,#cdbfa5 22%,#b9895e 45%,#8a5a3a 70%,#b98a63 100%)}
.hero-title{top:52px;width:100%;text-align:center;font-family:"Teko",sans-serif;font-weight:600;font-size:76px;line-height:.84;color:var(--ink);text-transform:uppercase}
.hero-title .accent{color:var(--blue)}
.hero-sub{top:180px;width:100%;text-align:center;font-size:22px;font-weight:500;color:var(--white);letter-spacing:1px;text-transform:uppercase}
.hero-btn{left:541px;top:228px;width:117px;height:41px;background:var(--red);color:var(--white)}
.dots{left:74px;top:552px;display:flex;gap:13px}
.dots span{width:11px;height:11px;border-radius:50%;background:var(--white)}
.dots span:first-child{background:var(--blue)}

/* events */
.events{height:603px}
.events .section-title{position:absolute;top:58px;width:100%}
.events .rule{position:absolute;top:110px;left:559px}
.card-row{position:absolute;left:75px;display:flex;gap:33px}
.event-card{width:329px}
.event-card .photo{height:193px}
.event-date{margin-top:19px;font-family:"Teko",sans-serif;font-weight:600;font-size:21px;color:var(--red);line-height:1}
.event-text{margin-top:10px;font-size:15.5px;line-height:23.5px;color:var(--ink)}
.card-btn{width:118px;height:42px;margin-top:33px}

/* gallery */
.gallery{height:543px;background:var(--grey-bg)}
.gallery .section-title{position:absolute;top:48px;width:100%}
.gallery .rule{position:absolute;top:104px;left:559px}
.gallery-grid{position:absolute;left:75px;top:151px;display:grid;grid-template-columns:repeat(4,252px);grid-template-rows:160px 160px;column-gap:14px;row-gap:14px}
.tall{grid-row:span 2}

/* ladder */
.ladder{height:599px}
.ladder .section-title{position:absolute;left:75px;top:44px;text-align:left}
.ladder .rule{position:absolute;top:106px;left:75px}
.ladder-arrows{left:1056px;top:49px;display:flex;gap:20px}
.ladder-card{width:329px}
.ladder-card .photo{height:194px}
.ladder-head{margin-top:22px;font-family:"Teko",sans-serif;font-weight:600;font-size:30px;line-height:1;color:var(--blue);text-transform:uppercase}
.ladder-text{margin-top:12px;font-size:15.5px;line-height:23.5px;color:var(--ink)}
.ladder-card .card-btn{margin-top:26px}

/* about */
.about{height:423px;background:linear-gradient(90deg,var(--blue-bright),var(--blue) 60%,#1d34a3)}
.about-photo{left:75px;top:60px;width:510px;height:302px;background:linear-gradient(180deg,#8a5a34,#a8754a 50%,#6d4526)}
.about-title{left:617px;top:62px;font-family:"Russo One",sans-serif;font-variant:small-caps;font-size:35px;line-height:39px;color:var(--white);letter-spacing:1px}
.about-text{left:617px;top:187px;width:512px;font-size:14.5px;line-height:26px;color:var(--white)}
.about-btn{left:617px;top:313px;width:117px;height:41px}

/* merchandise */
.merch{height:602px}
.merch .section-title{position:absolute;top:46px;width:100%}
.merch .rule{position:absolute;top:104px;left:559px}
.merch-row{position:absolute;left:75px;top:151px;display:flex;gap:29px}
.merch-card{width:242px;text-align:center}
.merch-box{height:205px;border:1.5px solid #555;display:flex;align-items:center;justify-content:center}
.merch-box .photo{width:150px;height:150px;border-radius:10px}
.merch-head{margin-top:22px;font-family:"Teko",sans-serif;font-weight:600;font-size:26px;line-height:1;color:var(--blue);text-transform:uppercase}
.merch-text{margin-top:6px;font-size:13px;line-height:25px;color:#333}
.merch-btn{margin:22px auto 0;width:118px;height:42px}

/* sponsors */
.sponsors{height:326px;background:linear-gradient(180deg,#1d3cae,#2047c4 50%,#173395)}
.sponsors .section-title{position:absolute;top:58px;width:100%;color:var(--white);font-size:33px}
.sponsors .rule{position:absolute;top:118px;left:560px;background:var(--white)}
.sponsor-row{left:74px;top:174px;width:1052px;display:flex;justify-content:space-between;align-items:center;font-size:31px;font-weight:600;color:var(--white)}

/* footer */
.site-footer{height:347px;background:var(--footer);color:var(--white)}
.foot-brand{left:78px;top:64px;width:198px;height:66px;display:flex;align-items:center;gap:10px;border:3px solid var(--white);border-radius:8px;padding:0 10px}
.foot-brand .brand-name{color:var(--white)}
.copyright{left:70px;top:134px;width:215px;text-align:center;font-size:11px;line-height:25px}
.socials{left:78px;top:226px;width:220px;display:flex;flex-wrap:wrap;column-gap:10px;row-gap:4px;font-size:11px;font-weight:500}
.foot-col{top:56px}
.foot-col h3{font-family:"Russo One",sans-serif;font-size:17px;letter-spacing:.5px;margin-bottom:14px}
.foot-about{left:341px;width:250px;font-size:12.5px;line-height:27px}
.foot-links{list-style:none;font-size:12.5px;font-weight:500;text-transform:uppercase;line-height:30.5px}
.newsletter{left:885px;width:242px}
.email{height:46px;background:var(--white);color:#222;font-size:12.5px;display:flex;align-items:center;padding-left:14px}
.subscribe{margin-top:18px;height:48px;font-size:15px}
</style>
</head>
<body>

<header class="site-header">
  <div class="abs brand"><span class="brand-mark"></span><span class="brand-name">Velo Dash Compact Speed Karts</span></div>
  <nav class="abs util-nav"><span>MERCHANDISE</span><span>CONTACT US</span></nav>
  <a class="abs login">MEMBER LOGIN</a>
  <nav class="abs main-nav">
    <span class="current">HOME</span><span>ABOUT US</span><span>CHAMPIONSHIP LADDER</span><span>PHOTO GALLERY</span><span>SPONSORS</span>
  </nav>
</header>

<section class="hero">
  <div class="hero-photo" role="img" aria-label="Three off-road buggies racing on a dusty dirt track"></div>
  <h1 class="abs hero-title">Velo Dash<br>Compact <span class="accent">Speed Karts</span></h1>
  <p class="abs hero-sub">Sed ut perspiciatis unde omnis iste natus error sit.</p>
  <a class="abs btn hero-btn">Read More</a>
  <div class="abs dots"><span></span><span></span><span></span><span></span></div>
</section>

<section class="events">
  <h2 class="section-title">Event Calendar</h2>
  <div class="rule"></div>
  <svg class="abs arrow" style="left:38px;top:242px" viewBox="0 0 26 44"><path d="M20 4 4 22l16 18" fill="none" stroke="#666" stroke-width="2.5"/></svg>
  <svg class="abs arrow" style="left:1137px;top:242px" viewBox="0 0 26 44"><path d="M6 4l16 18L6 40" fill="none" stroke="#666" stroke-width="2.5"/></svg>
  <div class="card-row" style="top:157px">
    <article class="event-card">
      <div class="photo" role="img" aria-label="Buggies kicking up dust on a dirt track" style="background:linear-gradient(180deg,#b8a590,#9b7b5c 55%,#7d5c40)"></div>
      <p class="event-date">SEP 28, 2023</p>
      <p class="event-text">Sed ut perspiciatis unde omnis iste natus error sit voluptatem accu santium doloremque.</p>
      <a class="btn btn-yellow card-btn">Read More</a>
    </article>
    <article class="event-card">
      <div class="photo" role="img" aria-label="Race cars lined up beside a checkered flag" style="background:linear-gradient(135deg,#3a3a3a,#c0692e 45%,#d8793a 70%,#9a4a22)"></div>
      <p class="event-date">SEP 28, 2023</p>
      <p class="event-text">Sed ut perspiciatis unde omnis iste natus error sit voluptatem accu santium doloremque.</p>
      <a class="btn btn-yellow card-btn">Read More</a>
    </article>
    <article class="event-card">
      <div class="photo" role="img" aria-label="Buggies racing on an asphalt track" style="background:linear-gradient(180deg,#6d6f68,#8b8d85 50%,#5c5e58)"></div>
      <p class="event-date">SEP 28, 2023</p>
      <p class="event-text">Sed ut perspiciatis unde omnis iste natus error sit voluptatem accu santium doloremque.</p>
      <a class="btn btn-yellow card-btn">Read More</a>
    </article>
  </div>
</section>

<section class="gallery">
  <h2 class="section-title">Photo Gallery</h2>
  <div class="rule"></div>
  <div class="gallery-grid">
    <div class="photo" role="img" aria-label="Blue buggy on dirt" style="background:linear-gradient(180deg,#4a3a2c,#8a6a4a)"></div>
    <div class="photo tall" role="img" aria-label="White and blue touring car on a track" style="background:linear-gradient(180deg,#7a6a5a,#b8b2b8 50%,#6e625a)"></div>
    <div class="photo" role="img" aria-label="Blue and orange buggy on dirt" style="background:linear-gradient(180deg,#c7c2b6,#a99a84)"></div>
    <div class="photo tall" role="img" aria-label="Buggy beside orange cones" style="background:linear-gradient(180deg,#1f1a14,#6a5a4a 45%,#b1a596)"></div>
    <div class="photo" role="img" aria-label="Green buggy on a dirt track" style="background:linear-gradient(180deg,#9a6a40,#b47c4a)"></div>
    <div class="photo" role="img" aria-label="Rally car near water" style="background:linear-gradient(180deg,#5f7d8a,#9ab0b8 60%,#485860)"></div>
  </div>
</section>

<section class="ladder">
  <h2 class="section-title">Championship Ladder</h2>
  <div class="rule"></div>
  <div class="abs ladder-arrows">
    <svg class="arrow" viewBox="0 0 26 44" style="height:38px"><path d="M20 4 4 22l16 18" fill="none" stroke="#666" stroke-width="2.5"/></svg>
    <svg class="arrow" viewBox="0 0 26 44" style="height:38px"><path d="M6 4l16 18L6 40" fill="none" stroke="var(--yellow)" stroke-width="3"/></svg>
  </div>
  <div class="card-row" style="top:140px">
    <article class="ladder-card">
      <div class="photo" role="img" aria-label="Buggies racing through dust" style="background:linear-gradient(180deg,#8a7a64,#b99a76 50%,#8b6a48)"></div>
      <h3 class="ladder-head">Sed ut perspiciatis</h3>
      <p class="ladder-text">Unde omnis &nbsp;iste natus error sit voluptatem accu santium dolor emq ue enim ipsam voluptatem.</p>
      <a class="btn btn-yellow card-btn">Read More</a>
    </article>
    <article class="ladder-card">
      <div class="photo" role="img" aria-label="Buggy chassis on a sandy track" style="background:linear-gradient(180deg,#d8c6a8,#b49a78 60%,#8f7658)"></div>
      <h3 class="ladder-head">Sed ut perspiciatis</h3>
      <p class="ladder-text">Unde omnis &nbsp;iste natus error sit voluptatem accu santium dolor emq ue enim ipsam voluptatem.</p>
      <a class="btn btn-yellow card-btn">Read More</a>
    </article>
    <article class="ladder-card">
      <div class="photo" role="img" aria-label="Blue buggy close-up on dirt" style="background:linear-gradient(180deg,#4a3a2c,#3a5aa8 45%,#7a5a3e)"></div>
      <h3 class="ladder-head">Sed ut perspiciatis</h3>
      <p class="ladder-text">Unde omnis &nbsp;iste natus error sit voluptatem accu santium dolor emq ue enim ipsam voluptatem.</p>
      <a class="btn btn-yellow card-btn">Read More</a>
    </article>
  </div>
</section>

<section class="about">
  <div class="abs about-photo" role="img" aria-label="Buggy with a yellow wing on a dirt track"></div>
  <h2 class="abs about-title">About Velo Dash<br>Compact Speed Karts</h2>
  <p class="abs about-text">Sed ut perspiciatis unde omnis iste natus error sit voluptatem accusantium doloremque laudantium, totam rem aperiam, eaque ipsa quae ab illo inventore veritatis et quasi architecto beatae vitae dicta sunt explicabo.</p>
  <a class="abs btn btn-yellow about-btn">Read More</a>
</section>

<section class="merch">
  <h2 class="section-title">Merchandise</h2>
  <div class="rule"></div>
  <svg class="abs arrow" style="left:36px;top:323px" viewBox="0 0 26 44"><path d="M20 4 4 22l16 18" fill="none" stroke="#222" stroke-width="2.5"/></svg>
  <svg class="abs arrow" style="left:1138px;top:323px" viewBox="0 0 26 44"><path d="M6 4l16 18L6 40" fill="none" stroke="#222" stroke-width="2.5"/></svg>
  <div class="merch-row">
    <article class="merch-card">
      <div class="merch-box"><div class="photo" role="img" aria-label="White mug with club print" style="background:linear-gradient(180deg,#f2f2f2,#d6d6d6)"></div></div>
      <h3 class="merch-head">Product Heading</h3>
      <p class="merch-text">Excepteur sint occaecat cupidatat non proident pariatur</p>
      <a class="btn btn-yellow merch-btn">More Info</a>
    </article>
    <article class="merch-card">
      <div class="merch-box"><div class="photo" role="img" aria-label="Black t-shirt with club print" style="background:linear-gradient(180deg,#3a3a3a,#1c1c1c)"></div></div>
      <h3 class="merch-head">Product Heading</h3>
      <p class="merch-text">Excepteur sint occaecat cupidatat non proident pariatur</p>
      <a class="btn btn-yellow merch-btn">More Info</a>
    </article>
    <article class="merch-card">
      <div class="merch-box"><div class="photo" role="img" aria-label="Black cap with club print" style="background:linear-gradient(180deg,#2e2e2e,#111)"></div></div>
      <h3 class="merch-head">Product Heading</h3>
      <p class="merch-text">Excepteur sint occaecat cupidatat non proident pariatur</p>
      <a class="btn btn-yellow merch-btn">More Info</a>
    </article>
    <article class="merch-card">
      <div class="merch-box"><div class="photo" role="img" aria-label="Grey hoodie with club print" style="background:linear-gradient(180deg,#b4b4b4,#8e8e8e)"></div></div>
      <h3 class="merch-head">Product Heading</h3>
      <p class="merch-text">Excepteur sint occaecat cupidatat non proident pariatur</p>
      <a class="btn btn-yellow merch-btn">More Info</a>
    </article>
  </div>
</section>

<section class="sponsors" role="img" aria-label="Blue-tinted rally car background">
  <h2 class="section-title">Sponsors</h2>
  <div class="rule"></div>
  <svg class="abs" style="left:48px;top:184px" width="14" height="24" viewBox="0 0 14 24"><path d="M11 2 2 12l9 10" fill="none" stroke="#fff" stroke-width="2"/></svg>
  <svg class="abs" style="left:1140px;top:184px" width="14" height="24" viewBox="0 0 14 24"><path d="M3 2l9 10-9 10" fill="none" stroke="#fff" stroke-width="2"/></svg>
  <div class="abs sponsor-row">
    <span>Brightwell</span><span>Kestrel Group</span><span>Marrowfield</span><span>Halden Freight</span>
  </div>
</section>

<footer class="site-footer">
  <div class="abs foot-brand"><span class="brand-mark"></span><span class="brand-name">Velo Dash Compact Speed Karts</span></div>
  <p class="abs copyright">Copyright © 2023 CompanyName<br>All Right Reserved</p>
  <div class="abs socials"><span>Chatter</span><span>Postly</span><span>Snapfeed</span><span>Linkwork</span><span>vid hub</span></div>
  <div class="abs foot-col foot-about">
    <h3>ABOUT US</h3>
    <p>Sed ut perspiciatis unde omnis iste natus error sit voluptatem acc usantium doloremque laudantium, totam rem aperiam, eaque ipsa quae ab illo inventore veritatis et quasi architecto beatae.</p>
  </div>
  <div class="abs foot-col" style="left:635px">
    <h3>SITE LINKS</h3>
    <ul class="foot-links">
      <li>Home</li><li>About Us</li><li>Championship Ladder</li><li>Photo Gallery</li><li>Sponsors</li><li>Merchandise</li><li>Contact Us</li>
    </ul>
  </div>
  <div class="abs foot-col newsletter">
    <h3>NEWSLETTER SIGN UP</h3>
    <div class="email">Enter Email Address</div>
    <a class="btn btn-yellow subscribe">Subscribe</a>
  </div>
</footer>

</body>
</html>
```